Electrical service van wrap design

I need a wrap design for a Kestine Service body van on a 2006 Brauch K420 cutaway extended van. Wrap is for top section of van above doors on service body and for cab front and sides ( fenders, doors and hood only). Business name to be “Steady Oak Electrical Services”. Color scheme we hope to use is a darker gray background with orange and black lettering and logo. Open to all designer input. Phone number to be selected to day .. will update

Target Market(s)

Electrical Service customers

Industry/Entity Type

Electrical

Font styles to use
Serif

Requirements
Must have
• Phone number, licensed, bonded and insured, existing steady oak logo, Slogan
Nice to have
• Top of utility box is meant to serve as primary advertising billboard. Doors and hood can have information or graphics in support of that.
Should not have
• Only cab front and sides and box top of both sides to have graphics. Roofs and lower boxes not included in project

```html
<!DOCTYPE html>
<html lang="en">
<head>
<meta charset="utf-8">
<title>Steady Oak Electric Services – Van Wrap</title>
<link rel="stylesheet" href="https://fonts.googleapis.com/css2?family=Montserrat:wght@700;800&family=Oswald:wght@500;600&display=swap">
<style>
  :root {
    --wrap-charcoal: #32363d;
    --wrap-orange: #d9784f;
    --box-white: #f4f4f2;
    --box-line: #c9cacc;
    --glass: #5a6068;
    --tire: #1e1f22;
    --hub: #b9bcc0;
    --trim: #8d9095;
    --taillight: #c8302c;
    --page: #ffffff;
    --text-light: #ffffff;
  }
  html, body { margin: 0; padding: 0; width: 1200px; height: 1200px; overflow: hidden; background: var(--page); }
  .wrap-sheet { display: block; width: 1200px; height: 1200px; }
  .wrap-dark { fill: var(--wrap-charcoal); }
  .wrap-accent { fill: var(--wrap-orange); }
  .box-body { fill: var(--box-white); stroke: var(--box-line); stroke-width: 1; }
  .panel-seam { stroke: var(--box-line); stroke-width: 1.2; fill: none; }
  .latch { fill: var(--trim); }
  .glass { fill: var(--glass); }
  .tire { fill: var(--tire); }
  .hub { fill: var(--hub); }
  .trim { fill: var(--trim); }
  .taillight { fill: var(--taillight); }
  .brand-name { font-family: "Montserrat", sans-serif; font-weight: 800; fill: var(--wrap-orange); }
  .brand-sub { font-family: "Montserrat", sans-serif; font-weight: 700; fill: var(--text-light); letter-spacing: 2px; }
  .phone { font-family: "Oswald", sans-serif; font-weight: 600; fill: var(--text-light); letter-spacing: 0.5px; }
  .web { font-family: "Oswald", sans-serif; font-weight: 600; fill: var(--wrap-orange); }
  .fine { font-family: "Oswald", sans-serif; font-weight: 500; fill: var(--text-light); }
</style>
</head>
<body>
<svg class="wrap-sheet" viewBox="0 0 960 960" xmlns="http://www.w3.org/2000/svg" role="img" aria-label="Steady Oak Electric Services van wrap: driver side, passenger side, front and rear views">
  <defs>
    <g id="side-body">
      <path class="wrap-dark" d="M155,78 Q155,68 165,68 L555,68 L558,152 L155,152 Z"/>
      <rect class="box-body" x="155" y="152" width="405" height="120" rx="3"/>
      <path class="panel-seam" d="M236,160 V268 M390,160 V268 M455,160 V268 M236,205 H390"/>
      <rect class="latch" x="168" y="206" width="10" height="6"/>
      <rect class="latch" x="308" y="160" width="8" height="10"/>
      <rect class="latch" x="400" y="206" width="10" height="6"/>
      <rect class="latch" x="462" y="206" width="10" height="6"/>
      <rect class="trim" x="130" y="268" width="430" height="8"/>
      <path class="wrap-dark" d="M555,100 L640,98 Q690,100 720,150 L790,178 Q806,188 808,240 L808,276 L555,280 Z"/>
      <path class="glass" d="M575,112 L648,110 Q668,114 690,150 L575,152 Z"/>
      <path fill="var(--box-white)" d="M555,188 L562,188 L606,250 L690,250 L690,274 L555,274 Z"/>
      <path fill="var(--box-white)" d="M533,152 L549,152 L622,234 L690,234 L690,240 L606,240 Z"/>
      <path class="wrap-accent" d="M155,154 L528,154 L606,240 L690,240 L690,258 L594,258 L518,162 L155,162 Z"/>
      <rect class="trim" x="560" y="274" width="120" height="8"/>
      <rect class="trim" x="782" y="236" width="30" height="40" rx="4"/>
      <circle class="tire" cx="315" cy="284" r="40"/>
      <circle class="hub" cx="315" cy="284" r="22"/>
      <circle class="tire" cx="730" cy="280" r="40"/>
      <circle class="hub" cx="730" cy="280" r="22"/>
    </g>
  </defs>

  <g class="side-view side-view--right">
    <use href="#side-body"/>
    <rect class="wrap-accent" x="177" y="74" width="64" height="64" rx="8"/>
    <text class="brand-name" x="254" y="110" font-size="33">STEADY OAK</text>
    <text class="brand-sub" x="290" y="133" font-size="13">ELECTRIC SERVICES</text>
    <text class="phone" x="588" y="191" font-size="16">912-555-0186</text>
    <text class="web" x="608" y="203" font-size="8">STEADYOAKHANDY.COM</text>
    <text class="fine" x="620" y="212" font-size="5.5">SERVING MARLOW BAY</text>
    <text class="fine" x="620" y="219" font-size="5.5">AND TERN ISLAND</text>
    <text class="fine" x="697" y="201" font-size="7">LICENSED, BONDED AND INSURED</text>
  </g>

  <g class="side-view side-view--left">
    <use href="#side-body" transform="translate(938,356) scale(-1,1)"/>
    <rect class="wrap-accent" x="402" y="430" width="64" height="64" rx="8"/>
    <text class="brand-name" x="479" y="466" font-size="33">STEADY OAK</text>
    <text class="brand-sub" x="515" y="489" font-size="13">ELECTRIC SERVICES</text>
    <text class="phone" x="255" y="546" font-size="16">912-555-0186</text>
    <text class="web" x="255" y="558" font-size="8">STEADYOAKHANDY.COM</text>
    <text class="fine" x="255" y="567" font-size="5.5">SERVING MARLOW BAY</text>
    <text class="fine" x="255" y="574" font-size="5.5">AND TERN ISLAND</text>
    <text class="fine" x="160" y="557" font-size="7">LICENSED, BONDED AND INSURED</text>
  </g>

  <g class="front-view">
    <path class="glass" d="M240,752 L412,752 L428,800 L224,800 Z"/>
    <path class="wrap-dark" d="M218,800 L436,800 L432,852 L222,852 Z"/>
    <rect class="trim" x="228" y="784" width="14" height="18" rx="2"/>
    <rect class="trim" x="412" y="784" width="14" height="18" rx="2"/>
    <rect class="wrap-accent" x="276" y="815" width="10" height="10"/>
    <text class="brand-name" x="292" y="825" font-size="13">STEADY OAK</text>
    <rect class="trim" x="268" y="850" width="120" height="32" rx="3"/>
    <rect class="box-body" x="226" y="852" width="36" height="18" rx="2"/>
    <rect class="box-body" x="394" y="852" width="36" height="18" rx="2"/>
    <rect class="trim" x="214" y="882" width="228" height="22" rx="4"/>
    <rect class="tire" x="228" y="904" width="30" height="30" rx="4"/>
    <rect class="tire" x="398" y="904" width="30" height="30" rx="4"/>
  </g>

  <g class="rear-view">
    <rect class="box-body" x="525" y="745" width="195" height="160" rx="4"/>
    <rect class="wrap-dark" x="560" y="760" width="130" height="122"/>
    <rect class="tire" x="580" y="787" width="22" height="32" rx="3"/>
    <rect class="tire" x="648" y="787" width="22" height="32" rx="3"/>
    <text class="fine" x="625" y="773" font-size="7" text-anchor="middle">LICENSED, BONDED AND INSURED</text>
    <rect class="wrap-accent" x="566" y="831" width="16" height="16" rx="2"/>
    <text class="brand-name" x="586" y="843" font-size="12.5">STEADY OAK</text>
    <text class="brand-sub" x="600" y="851" font-size="4.5" letter-spacing="1">ELECTRIC SERVICES</text>
    <rect class="wrap-accent" x="560" y="855" width="130" height="17"/>
    <text class="phone" x="625" y="869" font-size="13" text-anchor="middle">912-555-0186</text>
    <text class="fine" x="625" y="879" font-size="4.5" text-anchor="middle">SERVING MARLOW BAY AND TERN ISLAND</text>
    <circle class="taillight" cx="542" cy="790" r="5"/>
    <circle class="taillight" cx="542" cy="806" r="5"/>
    <circle class="taillight" cx="703" cy="790" r="5"/>
    <circle class="taillight" cx="703" cy="806" r="5"/>
    <rect class="trim" x="527" y="900" width="193" height="16" rx="2"/>
  </g>
</svg>
</body>
</html>
```